Quarlwick Builders Business Cards

I want to use the logo and make an unique business card that shows the textured Logo with brick and builings. I want to be able to stand out when I pass out business cards.

```html
<!DOCTYPE html>
<html lang="en">
<head>
<meta charset="UTF-8">
<title>Quarlwick Builders Business Cards</title>
<link href="https://fonts.googleapis.com/css2?family=Montserrat:wght@400;700&family=Roboto+Condensed:wght@700&display=swap" rel="stylesheet">
<style>
  :root {
    --backdrop: #3a3b3d;
    --card: #fdfdfd;
    --accent: #e8432a;
    --navy: #1b2747;
    --ink: #222222;
    --brick-light: #d9643f;
    --brick-dark: #8a3a26;
  }
  html, body {
    margin: 0;
    width: 1200px;
    height: 988px;
    overflow: hidden;
    background: var(--backdrop);
  }
  .sheet {
    position: relative;
    width: 1200px;
    height: 988px;
  }
  .card {
    position: absolute;
    left: 220px;
    width: 760px;
    height: 434px;
    background: var(--card);
    border-radius: 28px;
    border-bottom: 7px solid var(--accent);
    box-sizing: border-box;
    box-shadow: 0 18px 30px rgba(0,0,0,0.45);
  }
  .card--front { top: 34px; }
  .card--back  { top: 516px; }

  .brand {
    display: flex;
    flex-direction: column;
    align-items: center;
  }
  .brand__art {
    border-radius: 14px;
    background: linear-gradient(160deg, #a8593f 0%, var(--brick-light) 45%, var(--brick-dark) 100%);
  }
  .brand__name {
    font-family: "Roboto Condensed", sans-serif;
    font-weight: 700;
    color: var(--brick-dark);
    letter-spacing: 0.5px;
    text-transform: uppercase;
  }
  .brand__tagline {
    font-family: "Roboto Condensed", sans-serif;
    font-weight: 700;
    color: var(--navy);
  }

  .card--front .brand {
    position: absolute;
    left: 0; right: 0; top: 52px;
  }
  .card--front .brand__art { width: 380px; height: 220px; }
  .card--front .brand__name { font-size: 34px; margin-top: 14px; }
  .card--front .brand__tagline { font-size: 22px; margin-top: 6px; }

  .card--back .brand {
    position: absolute;
    right: 40px; top: 52px;
    width: 320px;
  }
  .card--back .brand__art { width: 300px; height: 172px; }
  .card--back .brand__name { font-size: 26px; margin-top: 12px; }
  .card--back .brand__tagline { font-size: 17px; margin-top: 4px; }

  .contact {
    position: absolute;
    left: 52px; top: 56px;
    font-family: "Montserrat", sans-serif;
    color: var(--ink);
  }
  .contact__name {
    margin: 0;
    font-size: 40px;
    font-weight: 700;
    color: var(--accent);
    letter-spacing: 0.5px;
  }
  .contact__title {
    margin: 4px 0 0;
    font-size: 19px;
  }
  .contact__address {
    margin: 34px 0 0 30px;
    font-style: normal;
    font-size: 19px;
    line-height: 1.3;
  }
  .contact__list {
    list-style: none;
    margin: 30px 0 0 30px;
    padding: 0;
    font-size: 19px;
  }
  .contact__list li {
    display: flex;
    align-items: center;
    gap: 12px;
    line-height: 1.45;
  }
  .contact__list svg { width: 17px; height: 17px; fill: var(--accent); flex: none; }
</style>
</head>
<body>
<main class="sheet">

  <section class="card card--front" aria-label="Card front">
    <div class="brand">
      <div class="brand__art" role="img" aria-label="Illustration of a brick city skyline with a brick wall and mason tools"></div>
      <div class="brand__name">Quarlwick Builders</div>
      <div class="brand__tagline">Pations-Sidewalks-Retaining Walls-Foundations</div>
    </div>
  </section>

  <section class="card card--back" aria-label="Card back">
    <div class="contact">
      <h1 class="contact__name">Dorian Kessler</h1>
      <p class="contact__title">Partner, Chief Officer</p>
      <address class="contact__address">
        48 Halvern Crescent,<br>
        Suite 210<br>
        Ashbury, ON K7P 2M9
      </address>
      <ul class="contact__list">
        <li><svg viewBox="0 0 24 24" aria-hidden="true"><path d="M6.6 10.8a15 15 0 0 0 6.6 6.6l2.2-2.2a1 1 0 0 1 1-.25 11.4 11.4 0 0 0 3.6.57 1 1 0 0 1 1 1V20a1 1 0 0 1-1 1A17 17 0 0 1 3 4a1 1 0 0 1 1-1h3.5a1 1 0 0 1 1 1c0 1.25.2 2.45.57 3.57a1 1 0 0 1-.25 1z"/></svg>555-014-2287</li>
        <li><svg viewBox="0 0 24 24" aria-hidden="true"><path d="M7 1h10a2 2 0 0 1 2 2v18a2 2 0 0 1-2 2H7a2 2 0 0 1-2-2V3a2 2 0 0 1 2-2zm0 3v14h10V4zm5 15.5a1.2 1.2 0 1 0 0 2.4 1.2 1.2 0 0 0 0-2.4z"/></svg>555-019-6431</li>
        <li><svg viewBox="0 0 24 24" aria-hidden="true"><path d="M2 5h20v14H2zm2 2v.5l8 5 8-5V7l-8 5z"/></svg>dorian.kessler@halvernco.com</li>
        <li><svg viewBox="0 0 24 24" aria-hidden="true"><path d="M12 2a10 10 0 1 0 0 20 10 10 0 0 0 0-20zm6.9 9h-3a15 15 0 0 0-1.3-5.6A8 8 0 0 1 18.9 11zM12 4.1c.9 1.3 1.8 3.6 1.9 6.9h-3.8c.1-3.3 1-5.6 1.9-6.9zM9.4 5.4A15 15 0 0 0 8.1 11h-3a8 8 0 0 1 4.3-5.6zM5.1 13h3a15 15 0 0 0 1.3 5.6A8 8 0 0 1 5.1 13zm6.9 6.9c-.9-1.3-1.8-3.6-1.9-6.9h3.8c-.1 3.3-1 5.6-1.9 6.9zm2.6-1.3a15 15 0 0 0 1.3-5.6h3a8 8 0 0 1-4.3 5.6z"/></svg>www.halvernco.com</li>
      </ul>
    </div>
    <div class="brand">
      <div class="brand__art" role="img" aria-label="Illustration of a brick city skyline with a brick wall and mason tools"></div>
      <div class="brand__name">Quarlwick Builders</div>
      <div class="brand__tagline">Pations-Sidewalks-Retaining Walls-Foundations</div>
    </div>
  </section>

</main>
</body>
</html>
```